Geschäftspapiere für Praxis für Integrative Physiotherapie
Zielgruppe
Praxis für Integrative Physiotherapie
Aufgabenstellung
Edel und übersichtlich, gern mit Farbe. Eventuell ein Wasserzeichen.
Logo gern in Relieflack oder als Metallic-Effekt gedruckt. Das neue Logo wurde bereits erstellt und befindet sich im Anhang! Im Anhang auch ein Bild von den aktuellen Visitenkarten!

```html
<!DOCTYPE html>
<html lang="de">
<head>
<meta charset="utf-8">
<title>Briefbogen – Praxis Auenlicht</title>
<link href="https://fonts.googleapis.com/css2?family=Josefin+Sans:wght@300;400;600;700&display=swap" rel="stylesheet">
<style>
  :root {
    --orange: #f5aa5c;
    --orange-text: #ee8a2f;
    --ink: #1b1b1b;
    --watermark: #fbe3cc;
    --fold: #7a7a7a;
    --backdrop: #ffffff;
  }
  * { margin: 0; padding: 0; box-sizing: border-box; }
  html, body { width: 1200px; height: 1200px; overflow: hidden; background: var(--backdrop); }
  body { font-family: "Josefin Sans", sans-serif; color: var(--ink); position: relative; }

  .letterhead {
    position: absolute; left: 175px; top: 0;
    width: 849px; height: 1200px;
    background: #fff; overflow: hidden;
  }
  .curves { position: absolute; inset: 0; width: 100%; height: 100%; }

  .watermark {
    position: absolute; left: -14px; top: 480px;
    width: 556px; height: 556px; border-radius: 50%;
    background: radial-gradient(circle, rgba(251,227,204,0.15) 40%, rgba(251,227,204,0.75) 62%, rgba(251,227,204,0.25) 72%, transparent 73%);
  }
  .corner-mark {
    position: absolute; left: 660px; top: 0; width: 190px; height: 180px;
    background: radial-gradient(circle at 60% 45%, rgba(247,210,175,0.55) 0%, rgba(247,210,175,0.2) 55%, transparent 70%);
  }

  .brand { position: absolute; right: 80px; top: 98px; text-align: right; }
  .brand-name { font-size: 34px; font-weight: 600; color: var(--orange-text); line-height: 1; }
  .brand-tagline { font-size: 16px; font-weight: 400; margin-top: 18px; letter-spacing: 0.2px; }

  .sender-line { position: absolute; left: 101px; top: 193px; font-size: 10px; font-weight: 400; }

  .person { position: absolute; right: 80px; top: 188px; text-align: right; font-size: 15px; line-height: 19px; font-weight: 300; }
  .person-name { font-weight: 600; font-size: 16px; }

  .fold-mark { position: absolute; left: 0; width: 14px; height: 1.5px; background: var(--fold); }
  .fold-mark.punch { height: 3px; }

  .footer { position: absolute; top: 1114px; font-size: 8px; font-weight: 600; line-height: 12.2px; }
  .footer-contact { left: 87px; }
  .footer-contact li { list-style: none; display: flex; align-items: center; gap: 8px; }
  .footer-contact svg { width: 8px; height: 8px; flex: none; }
  .footer-bank { left: 290px; }
  .footer-hours { left: 479px; }
  .footer-hours td { padding: 0; }
  .footer-hours td.day { width: 61px; }
</style>
</head>
<body>
<main class="letterhead">
  <svg class="curves" viewBox="0 0 849 1200" preserveAspectRatio="none" aria-hidden="true">
    <path d="M0 0 H168 Q70 14 0 58 Z" fill="var(--orange)"/>
    <path d="M849 1069 Q740 1160 487 1200 H849 Z" fill="var(--orange)"/>
  </svg>

  <div class="watermark" role="img" aria-label="Großes, zartes Praxiszeichen als Wasserzeichen"></div>
  <div class="corner-mark" role="img" aria-label="Zartes Praxiszeichen hinter dem Namenszug"></div>

  <header class="brand">
    <div class="brand-name">Praxis Auenlicht</div>
    <div class="brand-tagline">Praxis für integrative Physiotherapie</div>
  </header>

  <p class="sender-line">Praxis Auenlicht | Lindenweg 14 | 16321 Ladeburg</p>

  <div class="person">
    <div class="person-name">Tobias Wernke</div>
    <div>Physiotherapeut</div>
    <div>Masseur u. med. Bademeister</div>
    <div>Yogalehrer</div>
  </div>

  <span class="fold-mark" style="top:434px"></span>
  <span class="fold-mark punch" style="top:606px"></span>
  <span class="fold-mark" style="top:853px"></span>

  <ul class="footer footer-contact">
    <li><svg viewBox="0 0 10 10"><path d="M5 0.5a3.3 3.3 0 0 0-3.3 3.3C1.7 6.3 5 9.5 5 9.5s3.3-3.2 3.3-5.7A3.3 3.3 0 0 0 5 0.5z" fill="none" stroke="var(--orange)" stroke-width="1.2"/><circle cx="5" cy="3.8" r="1.1" fill="var(--orange)"/></svg>Lindenweg 14 | 16321 Bernau OT Ladeburg</li>
    <li><svg viewBox="0 0 10 10"><path d="M2 1l2 2-1 1.2c.6 1.3 1.5 2.2 2.8 2.8L7 6l2 2-1.2 1.5C4.5 9.2.8 5.5.5 2.2z" fill="none" stroke="var(--orange)" stroke-width="1"/></svg>033338&nbsp; 52814</li>
    <li><svg viewBox="0 0 10 10"><rect x="2.5" y="0.8" width="5" height="2.5" fill="var(--orange)"/><rect x="0.8" y="3.5" width="8.4" height="4" rx="1" fill="var(--orange)"/><rect x="2.5" y="6.5" width="5" height="2.8" fill="#fff" stroke="var(--orange)" stroke-width="0.8"/></svg>033338 527700</li>
    <li><svg viewBox="0 0 10 10"><rect x="0.8" y="2" width="8.4" height="6" fill="none" stroke="var(--orange)" stroke-width="1"/><path d="M0.8 2L5 5.5 9.2 2" fill="none" stroke="var(--orange)" stroke-width="1"/></svg>physiotherapie@praxis-auenlicht.de</li>
    <li><svg viewBox="0 0 10 10"><path d="M9.5 0.5L0.5 4.3 4.3 5.7 5.7 9.5z" fill="var(--orange)"/></svg>www.praxis-auenlicht.de</li>
  </ul>

  <div class="footer footer-bank">
    <div>Kreissparkasse Nordland</div>
    <div>IBAN: DE12 3456 7890 0012 3456 78</div>
    <div>BIC: NORDDEKSXXX</div>
    <div>St-Nr.: 071 318 02956</div>
    <div>IK - Nr.: 450381627</div>
  </div>

  <table class="footer footer-hours">
    <tr><td class="day">Montags</td><td>8:00 - 18:30</td></tr>
    <tr><td class="day">Dienstags</td><td>8:00 - 18:00</td></tr>
    <tr><td class="day">Mittwochs</td><td>8:00 - 18:30</td></tr>
    <tr><td class="day">Donnerstags</td><td>8:00 - 18:00</td></tr>
    <tr><td class="day">Freitags</td><td>8:00 - 13:00</td></tr>
  </table>
</main>
</body>
</html>
```